Refresh of graphic design for existing website

We would like to refresh our website. Please see the attached design specifications.

Industry/Entity Type

Graphic Design

```html
<!DOCTYPE html>
<html lang="en">
<head>
<meta charset="utf-8">
<title>Forge and Tool Guild</title>
<link href="https://fonts.googleapis.com/css2?family=Open+Sans:wght@400;600;700&family=Oswald:wght@500;700&display=swap" rel="stylesheet">
<style>
:root{
  --blue:#1f7fd1;
  --blue-dark:#176bb3;
  --ink:#2b2b2b;
  --muted:#7a7a7a;
  --line:#e3e3e3;
  --footer:#1e1e1e;
  --footer-bar:#151515;
  --footer-text:#a9a9a9;
  --light:#f4f4f4;
}
*{box-sizing:border-box;margin:0;padding:0}
html,body{width:742px;height:1200px;overflow:hidden;background:#fff}
body{font-family:"Open Sans",Arial,sans-serif;color:var(--ink);position:relative}
.header{height:74px;display:flex;align-items:center;justify-content:space-between;padding:0 30px}
.brand{display:flex;align-items:center;gap:8px}
.brand-dot{width:22px;height:22px;border-radius:50%;background:var(--blue)}
.brand-name{font-weight:700;font-size:12px;color:var(--blue);letter-spacing:.5px}
.header-right{display:flex;align-items:center;gap:12px;font-size:11px}
.call{color:var(--muted)}
.call b{color:var(--ink);font-size:13px}
.print-btn{background:#2f2f2f;color:#fff;font-size:9px;font-weight:700;padding:7px 12px;border-radius:2px;display:flex;align-items:center;gap:5px}
.nav{height:34px;background:var(--blue);display:flex;align-items:center;padding:0 30px;gap:13px}
.nav a{color:#fff;font-size:8px;font-weight:700;text-decoration:none;letter-spacing:.2px;white-space:nowrap}
.nav a.active{background:var(--blue-dark);padding:12px 8px;margin-left:-8px}
.search{margin-left:auto;width:115px;height:20px;background:#fff;border-radius:2px;display:flex;align-items:center;justify-content:flex-end;padding-right:5px;flex:none}
.hero{position:relative;height:397px;background:linear-gradient(100deg,#4f6f7a 0%,#7e9aa2 40%,#c9ccc9 62%,#b7432f 80%,#8f6b5a 100%)}
.hero-text{position:absolute;left:30px;top:105px;color:#fff}
.hero h1{font-family:"Oswald",Impact,sans-serif;font-weight:700;font-size:48px;line-height:1;letter-spacing:.5px;white-space:nowrap}
.hero p{font-family:"Oswald",Impact,sans-serif;font-weight:500;font-size:19px;line-height:1.25;margin-top:10px;width:360px}
.hero-btn{display:inline-block;margin-top:20px;border:2px solid #fff;color:#fff;font-size:11px;font-weight:700;padding:9px 18px;border-radius:3px}
.welcome{text-align:center;padding:26px 60px 0}
.welcome h2{font-size:19px;font-weight:700;letter-spacing:.3px}
.rule{width:40px;height:2px;background:var(--blue);margin:8px auto 10px}
.welcome p{font-size:7.5px;line-height:1.6;color:var(--muted)}
.cols{position:absolute;top:640px;left:30px;right:30px;display:flex;gap:15px}
.col{width:212px}
.col h3{font-size:12px;font-weight:700;margin-bottom:10px}
.thumb{height:88px;background:linear-gradient(135deg,#8c99a3,#5f6d78 60%,#c7b8a4)}
.thumb.news{background:linear-gradient(135deg,#6d7d86,#a8b2b7 50%,#3f5060)}
.col p{font-size:7px;line-height:1.55;color:var(--muted);margin:8px 0}
.more{display:inline-block;background:var(--blue);color:#fff;font-size:6.5px;font-weight:700;padding:4px 8px;border-radius:2px}
.quick{border:1px solid var(--line);width:213px;background:#fff}
.quick-head{background:var(--blue);color:#fff;text-align:center;font-size:11px;font-weight:700;padding:8px 0}
.quick li{list-style:none;display:flex;align-items:center;gap:10px;padding:9px 12px;border-bottom:1px solid var(--line);font-size:8.5px;font-weight:600;color:#444;text-transform:uppercase}
.quick li:last-child{border-bottom:none}
.ring{width:26px;height:26px;border-radius:50%;border:2px solid var(--blue);flex:none}
.about{position:absolute;top:862px;left:30px;width:440px}
.about h3{font-size:17px;font-weight:700}
.about .rule{margin:6px 0 8px}
.about p{font-size:7px;line-height:1.6;color:var(--muted);margin-bottom:8px}
.newsletter{position:absolute;top:866px;left:499px;width:213px;background:var(--light);border:1px solid var(--line);padding:12px}
.newsletter h3{font-size:15px;font-weight:700;color:#555}
.nl-input{height:22px;background:#fff;border:1px solid #ddd;margin:10px 0}
.nl-row{display:flex;align-items:center;justify-content:space-between;font-size:7px;color:var(--muted)}
.check{display:flex;align-items:center;gap:4px}
.box{width:8px;height:8px;border:1px solid #999;background:#fff}
.sub-btn{background:var(--blue);color:#fff;font-size:7px;font-weight:700;padding:5px 12px;border-radius:2px}
.footer{position:absolute;top:1000px;left:0;width:742px;height:175px;background:var(--footer);padding:20px 30px;display:flex;gap:30px;color:var(--footer-text)}
.f-col{flex:1}
.f-col h4{color:var(--blue);font-size:9px;font-weight:700;margin-bottom:6px}
.f-col .rule{margin:0 0 8px;width:25px}
.f-col li{list-style:none;font-size:7px;line-height:1.7}
.f-contact li{display:flex;gap:5px;align-items:center}
.f-contact svg{flex:none}
.post{margin-bottom:8px}
.post b{display:block;color:#ddd;font-size:7px}
.post span{font-size:6.5px;line-height:1.4;display:block}
.social li{display:flex;gap:5px;align-items:center}
.social .sq{width:8px;height:8px;background:var(--footer-text)}
.bottom{position:absolute;top:1175px;left:0;width:742px;height:25px;background:var(--footer-bar);color:#777;font-size:7px;display:flex;align-items:center;justify-content:center}
</style>
</head>
<body>
<header class="header">
  <div class="brand"><span class="brand-dot"></span><span class="brand-name">FORGE AND TOOL GUILD</span></div>
  <div class="header-right">
    <span class="call">Call Now: <b>555-014-0192</b></span>
    <span class="print-btn"><svg width="9" height="9" viewBox="0 0 10 10"><rect x="2" y="0" width="6" height="3" fill="#fff"/><rect x="0" y="3" width="10" height="4" fill="#fff"/><rect x="2" y="6" width="6" height="4" fill="#fff" stroke="#2f2f2f"/></svg>PRINTER FRIENDLY</span>
  </div>
</header>
<nav class="nav">
  <a class="active">HOME</a><a>ABOUT</a><a>MEMBERSHIP</a><a>FTG MEMBERS</a><a>FTG EVENTS</a><a>TOOLNET LIBRARY</a><a>MARKET RESEARCH</a><a>HIDDEN FILES</a>
  <span class="search"><svg width="9" height="9" viewBox="0 0 10 10"><circle cx="4" cy="4" r="3" fill="none" stroke="#555" stroke-width="1.4"/><line x1="6.3" y1="6.3" x2="9.5" y2="9.5" stroke="#555" stroke-width="1.4"/></svg></span>
</nav>
<section class="hero" role="img" aria-label="Photo of a smiling technician in a workshop holding a tool">
  <div class="hero-text">
    <h1>FORGE AND TOOL GUILD</h1>
    <p>PROVIDING PROFESSIONAL ACCOUNTING SERVICES, COMPANY INCORPORATION.</p>
    <span class="hero-btn">MORE INFO</span>
  </div>
</section>
<section class="welcome">
  <h2>WELCOME TO FORGE AND TOOL GUILD</h2>
  <div class="rule"></div>
  <p>Professional Services, our members provide trusted guidance and support for every stage of tool and equipment work. We help businesses grow through shared research, practical training, industry events and a strong network of partners who care about quality, safety and long lasting results across the whole trade.</p>
</section>
<div class="cols">
  <div class="col">
    <h3>UPCOMING EVENTS</h3>
    <div class="thumb" role="img" aria-label="Photo of members talking at an event"></div>
    <p>Join us for a series of workshops and meetings where members share new methods, review market trends and meet suppliers. Each session is open to guests, with time set aside for questions and networking after the talks.</p>
    <span class="more">READ MORE</span>
  </div>
  <div class="col">
    <h3>INDUSTRY NEWS</h3>
    <div class="thumb news" role="img" aria-label="Photo of a technician working on equipment"></div>
    <p>Read the latest updates from across the trade, from new service standards to changes in training rules. Our editors collect short reports each month so members can stay informed and plan ahead with confidence.</p>
    <span class="more">READ MORE</span>
  </div>
  <div class="quick">
    <div class="quick-head">QUICK LINKS</div>
    <ul>
      <li><span class="ring"></span>TOOLNET LIBRARY</li>
      <li><span class="ring"></span>FTG NEWS BLOG</li>
      <li><span class="ring"></span>FTG MEMBER COMPANIES</li>
      <li><span class="ring"></span>FTG'S ACTIVE PARTICIPANTS</li>
    </ul>
  </div>
</div>
<section class="about">
  <h3>ABOUT COMPANY</h3>
  <div class="rule"></div>
  <p>Founded by a group of makers and service firms, our guild brings companies together to share knowledge, set fair standards and support skilled work. Members gain access to research, training resources and a trusted community that helps them serve customers better every day, while new firms find guidance as they grow.</p>
  <span class="more">READ MORE</span>
</section>
<aside class="newsletter">
  <h3>NEWSLETTER</h3>
  <div class="nl-input"></div>
  <div class="nl-row"><span class="check"><span class="box"></span>Newsletter</span><span class="sub-btn">SUBSCRIBE</span></div>
</aside>
<footer class="footer">
  <div class="f-col">
    <h4>ABOUT US</h4><div class="rule"></div>
    <ul><li>Home</li><li>About</li><li>Membership</li><li>FTG Members</li><li>FTG Events</li><li>Toolnet Library</li><li>Market Research</li><li>Hidden Files</li></ul>
  </div>
  <div class="f-col f-contact">
    <h4>CONTACT US</h4><div class="rule"></div>
    <ul>
      <li><svg width="7" height="9" viewBox="0 0 10 13"><path d="M5 0a5 5 0 0 0-5 5c0 4 5 8 5 8s5-4 5-8a5 5 0 0 0-5-5z" fill="#a9a9a9"/></svg>4120 Harbor Lane, Suite 18,</li>
      <li style="padding-left:12px">Millbrook, ST 00451</li>
      <li><svg width="8" height="8" viewBox="0 0 10 10"><path d="M2 0l2 3-1 1.5c.8 1.4 1.8 2.4 3 3L7.5 6l2.5 2-1 2C4 10 0 6 0 1z" fill="#a9a9a9"/></svg>555-014-0192</li>
      <li><svg width="8" height="7" viewBox="0 0 10 8"><rect width="10" height="8" fill="#a9a9a9"/><path d="M0 0l5 4 5-4" fill="none" stroke="#1e1e1e"/></svg>info@forgetoolguild.example</li>
    </ul>
  </div>
  <div class="f-col">
    <h4>OUR BLOG</h4><div class="rule"></div>
    <div class="post"><b>Brightline Professional Services receives</b><span>New award for quality in service and training, shared with the team.</span></div>
    <div class="post"><b>Brightline Professional Services receives</b><span>Recognition for its work with members across the region this year.</span></div>
  </div>
  <div class="f-col social">
    <h4>SOCIAL MEDIA LINKS</h4><div class="rule"></div>
    <ul><li><span class="sq"></span>Social Page</li><li><span class="sq"></span>Updates Feed</li><li><span class="sq"></span>Community</li></ul>
  </div>
</footer>
<div class="bottom">Copyright © 2015 Forge and Tool Guild. All rights reserved.</div>
</body>
</html>
```